Brisk Tech Pathway by graduating students from college in two years

Based on the logo design, create stationary and business cards for
Dr. Velimir T Osunde, CEO, (703) 482-1630
and Mirela Thorpe, Respresentative, (301) 557-2048
Address: 4417 Marbleton Lane, Faurfax Station, VA 22061
Incorporate elelments of the logo

Target Market(s)

USA

Other font styles liked:
• match with the logo type style

```html
<!DOCTYPE html>
<html lang="en">
<head>
<meta charset="utf-8">
<title>Brisk Tech Pathway – Business Cards</title>
<link href="https://fonts.googleapis.com/css2?family=Montserrat:wght@500;600;700&display=swap" rel="stylesheet">
<style>
  :root {
    --board: #1b1b1b;
    --gold: #f8c42e;
    --navy: #0f2160;
    --paper: #ffffff;
    --trim: #c8102e;
  }
  * { box-sizing: border-box; margin: 0; padding: 0; }
  html, body { width: 1200px; height: 747px; overflow: hidden; background: var(--board); }
  body { position: relative; font-family: "Montserrat", Arial, sans-serif; }

  .divider { position: absolute; left: 586px; top: 0; width: 28px; height: 747px; background: var(--gold); }

  .bleed { position: absolute; width: 527px; height: 316px; border: 1px solid var(--trim); }
  .card {
    position: absolute; left: 18px; top: 18px; width: 490px; height: 280px;
    background: var(--paper); overflow: hidden;
  }
  .card::after {
    content: ""; position: absolute; left: 0; right: 0; bottom: 0; height: 15px; background: var(--gold);
  }

  .pos-tl { left: 30px; top: 38px; }
  .pos-tr { left: 643px; top: 38px; }
  .pos-bl { left: 30px; top: 394px; }
  .pos-br { left: 643px; top: 394px; }

  .brand {
    position: absolute; display: flex; flex-direction: column; align-items: center; text-align: center;
    color: var(--navy); font-weight: 700;
  }
  .brand-dot { border-radius: 50%; background: var(--gold); border: 4px solid var(--navy); }
  .card-front .brand { left: 30px; top: 86px; width: 155px; gap: 10px; font-size: 15px; line-height: 1.2; }
  .card-front .brand-dot { width: 44px; height: 44px; }
  .card-back .brand { left: 0; right: 0; top: 88px; gap: 14px; font-size: 26px; line-height: 1.2; }
  .card-back .brand-dot { width: 64px; height: 64px; border-width: 6px; }

  .holder { position: absolute; left: 221px; top: 56px; right: 14px; }
  .holder-name { color: var(--navy); font-weight: 600; font-size: 26px; line-height: 1.1; white-space: nowrap; }
  .holder-name.long { font-size: 23.5px; letter-spacing: -0.1px; padding-top: 2px; }
  .holder-role { color: var(--gold); font-weight: 600; font-size: 18px; margin-top: 6px; }
  .holder-role.small { font-size: 16px; margin-top: 8px; }

  .contact { position: absolute; left: 219px; top: 146px; color: var(--navy); font-weight: 500; font-size: 16.5px; line-height: 20px; }
  .contact-row { display: flex; align-items: flex-start; gap: 12px; }
  .contact-row + .contact-row { margin-top: 16px; }
  .contact-icon { width: 27px; height: 27px; border-radius: 50%; background: var(--navy); flex: none; display: flex; align-items: center; justify-content: center; }
  .contact-text { padding-top: 2px; white-space: nowrap; }
</style>
</head>
<body>
  <div class="divider"></div>

  <section class="bleed pos-tl">
    <div class="card card-front">
      <div class="brand"><span class="brand-dot"></span><span>Brisk Tech<br>Pathway</span></div>
      <div class="holder">
        <h1 class="holder-name long">Dr. Velimir T Osunde</h1>
        <p class="holder-role">CEO</p>
      </div>
      <div class="contact">
        <div class="contact-row">
          <span class="contact-icon"><svg width="15" height="15" viewBox="0 0 24 24"><path fill="#f8c42e" d="M6.6 10.8a15.1 15.1 0 0 0 6.6 6.6l2.2-2.2c.3-.3.7-.4 1-.2 1.1.4 2.3.6 3.6.6.6 0 1 .4 1 1V20c0 .6-.4 1-1 1A17 17 0 0 1 3 4c0-.6.4-1 1-1h3.5c.6 0 1 .4 1 1 0 1.3.2 2.5.6 3.6.1.3 0 .7-.2 1z"/></svg></span>
          <span class="contact-text">(703) 482-1630</span>
        </div>
        <div class="contact-row">
          <span class="contact-icon"><svg width="14" height="16" viewBox="0 0 24 28"><path fill="none" stroke="#f8c42e" stroke-width="2.4" d="M12 26s-8-8.5-8-14a8 8 0 0 1 16 0c0 5.5-8 14-8 14z"/><circle cx="12" cy="12" r="3" fill="none" stroke="#f8c42e" stroke-width="2.4"/></svg></span>
          <span class="contact-text">4417 Marbleton Lane,<br>Faurfax Station, VA 22061</span>
        </div>
      </div>
    </div>
  </section>

  <section class="bleed pos-tr">
    <div class="card card-front">
      <div class="brand"><span class="brand-dot"></span><span>Brisk Tech<br>Pathway</span></div>
      <div class="holder">
        <h1 class="holder-name">Mirela Thorpe</h1>
        <p class="holder-role small">Respresentative</p>
      </div>
      <div class="contact">
        <div class="contact-row">
          <span class="contact-icon"><svg width="15" height="15" viewBox="0 0 24 24"><path fill="#f8c42e" d="M6.6 10.8a15.1 15.1 0 0 0 6.6 6.6l2.2-2.2c.3-.3.7-.4 1-.2 1.1.4 2.3.6 3.6.6.6 0 1 .4 1 1V20c0 .6-.4 1-1 1A17 17 0 0 1 3 4c0-.6.4-1 1-1h3.5c.6 0 1 .4 1 1 0 1.3.2 2.5.6 3.6.1.3 0 .7-.2 1z"/></svg></span>
          <span class="contact-text">(301) 557-2048</span>
        </div>
        <div class="contact-row">
          <span class="contact-icon"><svg width="14" height="16" viewBox="0 0 24 28"><path fill="none" stroke="#f8c42e" stroke-width="2.4" d="M12 26s-8-8.5-8-14a8 8 0 0 1 16 0c0 5.5-8 14-8 14z"/><circle cx="12" cy="12" r="3" fill="none" stroke="#f8c42e" stroke-width="2.4"/></svg></span>
          <span class="contact-text">4417 Marbleton Lane,<br>Faurfax Station, VA 22061</span>
        </div>
      </div>
    </div>
  </section>

  <section class="bleed pos-bl">
    <div class="card card-back">
      <div class="brand"><span class="brand-dot"></span><span>Brisk Tech Pathway</span></div>
    </div>
  </section>

  <section class="bleed pos-br">
    <div class="card card-back">
      <div class="brand"><span class="brand-dot"></span><span>Brisk Tech Pathway</span></div>
    </div>
  </section>
</body>
</html>
```